The Harbor Post - Built for the Industry, by the Industry.

Looking for an email marketing Infographic I can send out via email to target Recruitment Firms letting them know we are launched! As of January 7th VALOKA is no longer allowing Recruitment Firms to post on their site unless you pay thousands of dollars a month. We are launching a site just for Recruiters to showcase their jobs. I have attached the almost completed website and a mocked up version of a simple infographic but we are looking for a WOW design that can get emailed out to 1000's of Recruitment Firms and they will just have to click the image to be taken to our site. I have added the colors and raleway - medium is the font on our site. Blue RGB: 8/113/182 Navy RGB: 27/32/48

Target Market(s)

Recruitment Firms Across Canada and the USA

Font styles to use
Other font styles liked:
• Very Open ...

Requirements
Must have
• WOW Factor, use of our Brand and Colours - raleway - medium is the font on our site. Blue RGB: 8/113/182 Navy RGB: 27/32/48. Our Logo and I have also attached our Landing Page ... down below.
Nice to have
• You can use "It's Time for Something New" or I'd be open to other ideas and taglines ... I'd like to see No Sponsored Jobs / No Pay-Per-Click / Flat Rates Only ...
• Our tagline is also - Built for the Industry, by the Industry"

```html
<!DOCTYPE html>
<html lang="en">
<head>
<meta charset="utf-8">
<title>The Harbor Post – Now Live for Recruiters</title>
<link rel="stylesheet" href="https://fonts.googleapis.com/css2?family=Raleway:wght@500;700;800&family=Open+Sans:wght@400&display=swap">
<style>
  :root {
    --navy: #2a2833;
    --orange: #f2861e;
    --blue: #1660ad;
    --label-blue: #1b5ea6;
    --ink: #1b2030;
    --white: #ffffff;
    --city-top: #f4f6f8;
    --city-bottom: #c3cfda;
  }
  * { margin: 0; padding: 0; box-sizing: border-box; }
  html, body { width: 734px; height: 1200px; overflow: hidden; background: var(--white); }
  .mailer {
    position: relative; width: 734px; height: 1200px; overflow: hidden;
    font-family: "Raleway", sans-serif; background: var(--white);
  }
  .skyline {
    position: absolute; left: 0; top: 500px; width: 734px; height: 623px;
    background: linear-gradient(180deg, var(--city-top) 0%, #e2e8ee 40%, var(--city-bottom) 100%);
  }
  .header-band { position: absolute; left: 0; top: 0; width: 734px; height: 600px; }
  .brand {
    position: absolute; top: 54px; left: 0; width: 734px;
    display: flex; justify-content: center; align-items: center; gap: 14px;
    color: var(--white); font-weight: 700; font-size: 34px; letter-spacing: 2px;
  }
  .brand-dot { width: 22px; height: 22px; border-radius: 50%; background: var(--white); }
  .headline {
    position: absolute; top: 206px; left: 0; width: 734px; text-align: center;
    color: var(--orange); font-weight: 700; font-size: 66px; line-height: 76px;
  }
  .benefit {
    position: absolute; top: 476px; width: 250px; margin-left: -125px;
    display: flex; flex-direction: column; align-items: center;
  }
  .benefit-ring {
    width: 170px; height: 170px; border-radius: 50%;
    border: 14px solid var(--orange); background: var(--white);
    display: flex; align-items: center; justify-content: center;
  }
  .benefit-label {
    margin-top: 14px; text-align: center; color: var(--label-blue);
    font-weight: 700; font-size: 24px; line-height: 30.5px; text-transform: uppercase;
  }
  .cta {
    position: absolute; left: 211px; top: 822px; width: 310px; height: 88px;
    border-radius: 44px; background: var(--blue); color: var(--white);
    display: flex; align-items: center; justify-content: center;
    font-weight: 700; font-size: 29px;
  }
  .contact {
    position: absolute; left: 98px; top: 962px; width: 536px; height: 86px;
    border-radius: 43px; background: var(--white); box-shadow: 0 4px 10px rgba(0,0,0,0.18);
    display: flex; align-items: center; justify-content: center; gap: 16px;
    color: var(--ink); font-weight: 700; font-size: 29px;
  }
  .footer {
    position: absolute; left: 0; top: 1123px; width: 734px; height: 77px;
    background: var(--navy); color: var(--white);
    display: flex; align-items: center; justify-content: center;
    font-family: "Open Sans", sans-serif; font-size: 20px;
  }
</style>
</head>
<body>
<main class="mailer">
  <div class="skyline" role="img" aria-label="Faded photograph of a city skyline with high-rise towers"></div>

  <svg class="header-band" width="734" height="600" viewBox="0 0 734 600" aria-hidden="true">
    <polygon points="0,0 734,0 734,514 0,576" fill="var(--navy)"/>
  </svg>

  <div class="brand"><span class="brand-dot"></span><span>THE HARBOR POST</span></div>

  <h1 class="headline">WE'RE LIVE FOR<br>RECRUITERS</h1>

  <section class="benefit" style="left:139px">
    <div class="benefit-ring">
      <svg width="96" height="80" viewBox="0 0 96 80" fill="none" stroke="var(--orange)" stroke-width="3" stroke-linejoin="round" stroke-linecap="round" aria-hidden="true">
        <circle cx="48" cy="14" r="7"/><circle cx="30" cy="18" r="6"/><circle cx="66" cy="18" r="6"/>
        <path d="M20 38c0-8 6-12 10-12M76 38c0-8-6-12-10-12M36 36c0-9 5-13 12-13s12 4 12 13"/>
        <path d="M4 46l16-6 10 20-14 6z M92 46l-16-6-10 20 14 6z"/>
        <path d="M30 58l14 12c3 2 6 2 8 0l14-12M40 48l12-4 14 12"/>
      </svg>
    </div>
    <p class="benefit-label">No sponsored<br>jobs, no<br>pay-per-click</p>
  </section>

  <section class="benefit" style="left:370px">
    <div class="benefit-ring">
      <svg width="80" height="68" viewBox="0 0 80 68" fill="none" stroke="var(--orange)" stroke-width="4" stroke-linejoin="round" aria-hidden="true">
        <rect x="4" y="16" width="72" height="48" rx="5"/>
        <path d="M28 16V8h24v8"/>
        <path d="M4 34h72"/>
        <rect x="35" y="29" width="10" height="10" rx="1"/>
      </svg>
    </div>
    <p class="benefit-label">Showcase your<br>jobs at<br>flat rates only</p>
  </section>

  <section class="benefit" style="left:603px">
    <div class="benefit-ring">
      <svg width="80" height="80" viewBox="0 0 80 80" fill="none" stroke="var(--orange)" stroke-width="3.5" stroke-linejoin="round" aria-hidden="true">
        <circle cx="40" cy="10" r="6"/><rect x="31" y="19" width="18" height="10" rx="3"/>
        <path d="M40 30v12M40 42l-22 10M40 42l22 10"/>
        <circle cx="15" cy="54" r="6"/><rect x="6" y="63" width="18" height="10" rx="3"/>
        <circle cx="65" cy="54" r="6"/><rect x="56" y="63" width="18" height="10" rx="3"/>
      </svg>
    </div>
    <p class="benefit-label">Built for the<br>industry,<br>by the<br>industry</p>
  </section>

  <div class="cta">POST YOUR JOBS</div>

  <div class="contact">
    <svg width="30" height="22" viewBox="0 0 30 22" aria-hidden="true">
      <rect x="0" y="0" width="30" height="22" rx="2" fill="var(--ink)"/>
      <path d="M2 3l13 10 13-10" fill="none" stroke="var(--white)" stroke-width="2.4"/>
    </svg>
    <span>info@theharborpost.com</span>
  </div>

  <footer class="footer">It's time for something new&nbsp;·&nbsp;© The Harbor Post</footer>
</main>
</body>
</html>
```